New Website for Manufacturing Company - PSD only, no coding - CLOSED TO NEW DESIGNERS

IF YOU HAVE NOT ALREADY SUBMITTED A DESIGN PLEASE DO NOT SUBMIT ONE.
This is a re-work of an existing website. We can keep the themes and color schemes the same but we will be changing the layout and page content.
The scope includes the creation of some icons/sketches that will form some of the page content.
The scope is design only, no coding.
There are four files that have been uploaded that give a more detailed project brief, please read them.
Target Market(s)
Manufacturing
Industry/Entity Type
It Company
Number of Pages Required
1 page
Look and feel
Each slider illustrates characteristics of the customer's brand and the style your logo design should communicate.

```html
<!DOCTYPE html>
<html lang="en">
<head>
<meta charset="utf-8">
<title>Corvane – High Temperature Insulation Experts</title>
<link href="https://fonts.googleapis.com/css2?family=Open+Sans:wght@400;600;700&display=swap" rel="stylesheet">
<style>
:root{
  --blue:#1d6fb8;
  --blue-dark:#155a97;
  --text:#555;
  --muted:#888;
  --line:#e3e3e3;
  --bg:#ffffff;
  --soft:#f6f6f6;
  --footer:#1f2326;
  --footer-bottom:#171a1c;
  --footer-text:#9aa0a4;
}
*{box-sizing:border-box;margin:0;padding:0}
html,body{width:1200px;height:2308px;overflow:hidden}
body{font-family:"Open Sans",Arial,sans-serif;color:var(--text);background:var(--bg);font-size:12px}
.container{width:1008px;margin:0 auto}

/* header */
.site-header{height:88px;display:flex;align-items:center;justify-content:space-between;padding:0 32px;border-bottom:1px solid var(--line)}
.brand{display:flex;align-items:center;gap:18px}
.brand-name{background:var(--blue);color:#fff;font-weight:700;font-size:22px;letter-spacing:1px;padding:8px 14px}
.brand-tagline{font-size:13px;color:#444;font-style:italic}
.header-contact{display:flex;align-items:center;gap:20px;font-size:12px;color:#555}
.header-contact span{display:flex;align-items:center;gap:6px}
.header-btn{background:var(--blue);color:#fff;font-size:11px;font-weight:600;padding:8px 16px;border-radius:3px;text-transform:uppercase}

/* hero */
.hero{position:relative;height:512px;background:linear-gradient(100deg,#3c4145 0%,#5d6368 45%,#3b4043 100%);color:#fff}
.hero-visual{position:absolute;left:110px;top:30px;width:420px;height:450px;background:radial-gradient(ellipse at center,#c9ccce 0%,#8d9296 55%,rgba(90,95,100,0) 80%)}
.hero-copy{position:absolute;left:600px;top:150px;width:480px}
.hero-copy h1{font-size:25px;font-weight:700;line-height:1.3}
.hero-copy h2{font-size:22px;font-weight:400;line-height:1.3;margin-bottom:14px}
.hero-copy p{font-size:13px;line-height:1.6;color:#e6e6e6;margin-bottom:26px}
.btn-outline{display:inline-block;border:2px solid #fff;color:#fff;font-size:11px;font-weight:700;padding:10px 20px;border-radius:3px}
.hero-arrow{position:absolute;top:236px;width:40px;height:40px;border-radius:50%;background:rgba(255,255,255,.15);display:flex;align-items:center;justify-content:center}
.hero-arrow.prev{left:20px}.hero-arrow.next{right:20px}

/* welcome */
.welcome{text-align:center;padding:56px 0 50px;border-bottom:1px solid var(--line)}
.welcome h2{color:var(--blue);font-size:26px;font-weight:600;margin-bottom:10px}
.welcome .lead{font-size:13px;color:#666;margin-bottom:14px}
.welcome p.body{font-size:11px;color:var(--muted);line-height:1.9;width:900px;margin:0 auto}
.btn-blue{display:inline-block;margin-top:22px;border:1px solid var(--blue);color:var(--blue);font-size:10px;font-weight:700;padding:9px 18px;border-radius:3px}

/* capabilities */
.capabilities{padding:48px 0 48px}
.capabilities h2{color:var(--blue);font-size:26px;font-weight:600}
.capabilities .lead{font-size:13px;color:#666;margin:6px 0 30px}
.card-grid{display:grid;grid-template-columns:repeat(4,234px);gap:26px 24px}
.card{border:1px solid var(--line);height:356px;background:#fff}
.card-visual{height:200px;margin:10px;background:linear-gradient(180deg,#f4f4f4,#dcdcdc)}
.card h3{color:var(--blue);font-size:14px;font-weight:600;padding:4px 14px 8px}
.card p{font-size:10.5px;color:var(--muted);line-height:1.75;padding:0 14px}
.card .more{display:block;padding:10px 14px;font-size:10px;color:var(--blue);font-weight:600}

/* news */
.news{background:var(--blue);color:#fff;height:232px;padding-top:30px}
.news h2{font-size:20px;font-weight:600;margin-bottom:20px}
.news-list{display:grid;grid-template-columns:1fr 1fr;gap:48px}
.news-item h3{font-size:12px;font-weight:600;margin-bottom:8px}
.news-item p{font-size:10.5px;line-height:1.75;color:#dbe8f5}
.news-item .date{margin-top:12px;font-size:10px;color:#fff;display:flex;align-items:center;gap:6px}

/* footer */
.site-footer{background:var(--footer);height:220px;padding-top:36px}
.footer-cols{display:grid;grid-template-columns:248px 216px 224px 248px 1fr}
.footer-cols h4{color:#fff;font-size:13px;font-weight:600;margin-bottom:14px}
.footer-cols li{list-style:none;font-size:10.5px;color:var(--footer-text);line-height:2}
.footer-bottom{background:var(--footer-bottom);height:48px}
.footer-bottom .container{display:flex;justify-content:space-between;align-items:center;height:48px;font-size:10px;color:var(--footer-text)}
.social{display:flex;gap:8px;align-items:center}
.social i{display:block;width:22px;height:22px;border-radius:50%;background:#3a7fc0}
.social i:nth-child(2){background:#2fa6d9}.social i:nth-child(3){background:#cf3b2e}.social i:nth-child(4){background:#2b5c9c}
</style>
</head>
<body>

<header class="site-header">
  <div class="brand">
    <div class="brand-name">CORVANE</div>
    <div class="brand-tagline">"High Temperature Insulation Experts"</div>
  </div>
  <div class="header-contact">
    <span><svg width="12" height="12" viewBox="0 0 24 24"><path fill="#1d6fb8" d="M6.6 10.8a15 15 0 0 0 6.6 6.6l2.2-2.2a1 1 0 0 1 1-.25 11.4 11.4 0 0 0 3.6.6 1 1 0 0 1 1 1V20a1 1 0 0 1-1 1A17 17 0 0 1 3 4a1 1 0 0 1 1-1h3.5a1 1 0 0 1 1 1c0 1.25.2 2.45.6 3.6a1 1 0 0 1-.25 1z"/></svg>(555) 014-2290</span>
    <span><svg width="13" height="10" viewBox="0 0 26 20"><rect x="1" y="1" width="24" height="18" fill="none" stroke="#1d6fb8" stroke-width="2"/><path d="M1 1l12 10L25 1" fill="none" stroke="#1d6fb8" stroke-width="2"/></svg>hello@corvane.com</span>
    <span class="header-btn">RFQ</span>
    <span class="header-btn">Contact</span>
  </div>
</header>

<section class="hero">
  <div class="hero-visual" role="img" aria-label="Industrial slitting and rewinding machine"></div>
  <div class="hero-copy">
    <h1>Manufacturer Fabricator and DIstributors</h1>
    <h2>of High Temprature Insulating Materials.!</h2>
    <p>With righteous indignation and dislike men who are so beguiled and demoralized by the charms of pleasure of the moment, so blinded by desire, foresee trouble.</p>
    <span class="btn-outline">VIEW MORE INFO</span>
  </div>
  <span class="hero-arrow prev"><svg width="12" height="16" viewBox="0 0 12 16"><path d="M9 2L3 8l6 6" fill="none" stroke="#fff" stroke-width="2"/></svg></span>
  <span class="hero-arrow next"><svg width="12" height="16" viewBox="0 0 12 16"><path d="M3 2l6 6-6 6" fill="none" stroke="#fff" stroke-width="2"/></svg></span>
</section>

<section class="welcome">
  <h2>Welcome To Corvane</h2>
  <p class="lead">Simply dummy text of the printing and typesetting industry. Lorem Ipsum has been the industry's standard</p>
  <p class="body">Sed ut perspiciatis unde omnis iste natus error sit voluptatem accusantium doloremque laudantium, totam rem aperiam, eaque ipsa quae ab illo inventore veritatis et quasi architecto beatae vitae dicta sunt explicabo. Nemo enim ipsam voluptatem quia voluptas sit aspernatur aut odit aut fugit, sed quia consequuntur magni dolores eos qui ratione voluptatem sequi nesciunt.</p>
  <span class="btn-blue">READ MORE</span>
</section>

<section class="capabilities container">
  <h2>Capabilities</h2>
  <p class="lead">Simply dummy text of the printing and typesetting industry. Lorem Ipsum has been the industry's standard</p>
  <div class="card-grid">
    <article class="card"><div class="card-visual" role="img" aria-label="Waterjet cutting machine sketch"></div><h3>Waterjet Cutting</h3><p>Ut enim ad minima veniam quis nostrum exercitationem ullam corporis suscipit laboriosam nisi aliquid.</p><span class="more">Read More ›</span></article>
    <article class="card"><div class="card-visual" role="img" aria-label="Coating machine sketch"></div><h3>Coating</h3><p>Ut enim ad minima veniam quis nostrum exercitationem ullam corporis suscipit laboriosam nisi aliquid.</p><span class="more">Read More ›</span></article>
    <article class="card"><div class="card-visual" role="img" aria-label="Laminating machine sketch"></div><h3>Laminating</h3><p>Ut enim ad minima veniam quis nostrum exercitationem ullam corporis suscipit laboriosam nisi aliquid.</p><span class="more">Read More ›</span></article>
    <article class="card"><div class="card-visual" role="img" aria-label="CNC machining center sketch"></div><h3>CNC Machining</h3><p>Ut enim ad minima veniam quis nostrum exercitationem ullam corporis suscipit laboriosam nisi aliquid.</p><span class="more">Read More ›</span></article>
    <article class="card"><div class="card-visual" role="img" aria-label="Slitting machine sketch"></div><h3>Slitting</h3><p>Ut enim ad minima veniam quis nostrum exercitationem ullam corporis suscipit laboriosam nisi aliquid.</p><span class="more">Read More ›</span></article>
    <article class="card"><div class="card-visual" role="img" aria-label="Die cutting press sketch"></div><h3>Die Cutting</h3><p>Ut enim ad minima veniam quis nostrum exercitationem ullam corporis suscipit laboriosam nisi aliquid.</p><span class="more">Read More ›</span></article>
    <article class="card"><div class="card-visual" role="img" aria-label="Vacuum forming machine sketch"></div><h3>Vacuum Formings</h3><p>Ut enim ad minima veniam quis nostrum exercitationem ullam corporis suscipit laboriosam nisi aliquid.</p><span class="more">Read More ›</span></article>
    <article class="card"><div class="card-visual" role="img" aria-label="Rewinding machine sketch"></div><h3>Other One</h3><p>Ut enim ad minima veniam quis nostrum exercitationem ullam corporis suscipit laboriosam nisi aliquid.</p><span class="more">Read More ›</span></article>
  </div>
</section>

<section class="news">
  <div class="container">
    <h2>Latest News</h2>
    <div class="news-list">
      <div class="news-item">
        <h3>We denounce with righteous indignation and dislike</h3>
        <p>Nam libero tempore, cum soluta nobis est eligendi optio cumque nihil impedit quo minus id quod maxime placeat facere possimus, omnis voluptas assumenda.</p>
        <div class="date"><svg width="10" height="10" viewBox="0 0 10 10"><rect x="0.5" y="1.5" width="9" height="8" fill="none" stroke="#fff"/></svg>August 12, 2015</div>
      </div>
      <div class="news-item">
        <h3>We denounce with righteous indignation and dislike</h3>
        <p>Nam libero tempore, cum soluta nobis est eligendi optio cumque nihil impedit quo minus id quod maxime placeat facere possimus, omnis voluptas assumenda.</p>
        <div class="date"><svg width="10" height="10" viewBox="0 0 10 10"><rect x="0.5" y="1.5" width="9" height="8" fill="none" stroke="#fff"/></svg>August 12, 2015</div>
      </div>
    </div>
  </div>
</section>

<footer>
  <div class="site-footer">
    <div class="container footer-cols">
      <div><h4>Capabilities</h4><ul><li>Cutting</li><li>Layout &amp; Design</li><li>Adhesive Application</li><li>Vacuum Forming</li></ul></div>
      <div><h4>Services</h4><ul><li>Design</li><li>Rapid Prototyping</li><li>Kitting</li><li>Warehousing</li></ul></div>
      <div><h4>Markets</h4><ul><li>Appliance</li><li>Automotive</li><li>Glass</li><li>Aerospace</li></ul></div>
      <div><h4>Documentation</h4><ul><li>Catalog</li><li>Data Sheets</li><li>Safety Sheets</li><li>Quality Certificates</li></ul></div>
      <div><h4>Contact Us</h4><ul><li>Request a Quote</li><li>Locations</li><li>Careers</li></ul></div>
    </div>
  </div>
  <div class="footer-bottom">
    <div class="container">
      <span>Copyright © Corvane 2015 — All Rights Reserved</span>
      <div class="social"><span>Connect With Us</span><i></i><i></i><i></i><i></i></div>
    </div>
  </div>
</footer>

</body>
</html>
```